Electrical & Communications Company Wordpress Themed Website Design

Hi everyone,

I need a wordpress themed website designed for a new company based in Sydney Australia called "TRELVEX". It delivers electrical and communication services to the domestic and commercial sectors.

It needs to be the FULL/COMPLETE wordpress theme! A clean and easy to use site.

Please guys take the time to look at these competitors sites:

www.quobble.com.au
www.zirconvoltworks.com.au
www.ubt.com.au
www.tallowwiring.com.au
www.wrightbergwire.com.au
www.gullivarwiremen.com.au

Please use these site for ideas only!!! we want to be original.

(If you would like to add electrical and communications to the logo that is O.K.)

Note: These logo's are registered trademarks of trelvex pty ltd.

Accreditation:

Bufo member (United cabling and signalling trades guild)

PLEASE CHECK THE WEB PLANNING LAYOUT BELOW FOR ROUGH IDEA

Have requested to increase payment to $400 and now guarantee payment!

Hi guys, forgot to mention i would like to see the business phone number prominently some where with a call to action.As we are a service business and need people to easly be able to see our contact number. Maybe top right courner but open to ideas. 

 Guys/Girls this is for a complete working word press theme that i can load up on the sever and access thru wordpress admin. Code etc

• - Logo Provided must be used
• - Themes and colours to be consisted with with brand
• - Fully customizable
• - Have a social share button from pinquo.com
• - Must be the full/complete theme for word press
• - zenpixbanks
• - contactform
• - would like orbe lumo charge bitfen displayed
• - Guarantee logo or something
• - Please don't waste your or our time submitting templates or copies of other sites original only!

```html
<!DOCTYPE html>
<html lang="en">
<head>
<meta charset="utf-8">
<title>TRELVEX – Electrical &amp; Communications</title>
<link href="https://fonts.googleapis.com/css2?family=Arimo:ital,wght@0,400;0,700;1,400&family=Exo+2:ital,wght@0,700;1,400&display=swap" rel="stylesheet">
<style>
:root{
  --page:#444548;
  --panel:#38393b;
  --panel-dark:#353638;
  --rule:#5a5b5e;
  --text:#d4d4d4;
  --muted:#a8a8a8;
  --red:#d91c24;
  --field:#c4c4c4;
  --header-top:#ffffff;
  --header-bottom:#c3c4c6;
}
*{margin:0;padding:0;box-sizing:border-box}
html,body{width:1200px;height:1125px;overflow:hidden}
body{background:var(--page);font-family:"Arimo",Arial,sans-serif;color:var(--text);position:relative}
.abs{position:absolute}
.header-band{left:0;top:0;width:1200px;height:218px;background:linear-gradient(var(--header-top) 0%,#ececed 40%,var(--header-bottom) 100%);border-top:4px solid #2e2f31;border-bottom:1px solid #2a2b2d}
.brand{left:136px;top:48px;display:flex;align-items:center;gap:10px}
.brand-dot{width:46px;height:46px;border-radius:50%;background:var(--red)}
.brand-name{font-weight:700;font-size:38px;color:var(--red);letter-spacing:1px}
.nav{left:524px;top:58px;display:flex;gap:5px}
.nav a{display:block;width:104px;height:29px;line-height:29px;text-align:center;color:#fff;font-size:12px;font-weight:700;text-decoration:none;border-radius:3px;background:linear-gradient(#6a6b6d,#3e3f41);border:1px solid #2e2f31}
.nav a.active{background:linear-gradient(#f0363c,#b2141b);border-color:#8e0f14}
.hero{left:183px;top:142px;width:609px;height:265px;border:2px solid #e6e6e6;box-shadow:0 2px 8px rgba(0,0,0,.5);background:linear-gradient(100deg,#2e4f86 0%,#3b5b8f 25%,#e8e6e2 50%,#f2f0ec 100%)}
.cta-title{left:843px;top:189px;font-family:"Exo 2",sans-serif;font-size:20px;color:#2a2a2c}
.cta-title b{font-weight:700}
.cta-title i{font-weight:400}
.cta-sub{left:843px;top:221px;font-family:"Exo 2",sans-serif;font-style:italic;font-size:16px;line-height:18.5px;color:#eee}
.cta-phone{left:843px;top:296px;font-family:"Exo 2",sans-serif;font-size:28px;color:#eee}
.cta-btn{left:844px;top:337px;width:194px;height:48px;border-radius:4px;background:linear-gradient(#f03238,#b0141a);display:flex;align-items:center;padding-left:48px;color:#fff;text-decoration:none;font-family:"Exo 2",sans-serif;font-weight:700;font-size:16px;line-height:16px}
.cta-btn::before{content:"";position:absolute;left:8px;top:10px;width:28px;height:28px;border-radius:50%;background:#1d1d1f;border:3px solid #888}
.rule-h{height:1px;background:var(--rule)}
.rule-v{width:1px;background:var(--rule)}
.intro{left:184px;top:489px;width:605px;font-size:11.2px;line-height:13.2px;letter-spacing:-.1px}
.intro b{font-weight:700}
.sector{width:196px;height:214px;background:#38393b}
.sector .pic{position:absolute;left:4px;top:4px;width:188px;height:175px}
.sector .label{position:absolute;left:0;top:183px;width:196px;height:31px;background:#3a3b3d;font-size:11.5px;line-height:31px;padding-left:9px;color:#ddd}
.sector .label::after{content:"";position:absolute;right:15px;top:12px;border:4px solid transparent;border-left:6px solid var(--red)}
.pitch{left:184px;top:790px;width:600px;font-size:11.2px;line-height:13.2px;letter-spacing:-.1px}
.services-title{left:184px;top:841px;font-size:11.5px}
.services{left:184px;top:873px;width:609px;height:116px;background:var(--panel-dark)}
.services li{position:absolute;list-style:none;font-size:11.5px;color:#ddd;padding-left:15px}
.services li::before{content:"";position:absolute;left:0;top:3px;border:3px solid transparent;border-left:5px solid var(--red)}
.form-panel{left:825px;top:467px;width:212px;height:327px;background:var(--panel)}
.pay-panel{left:825px;top:806px;width:212px;height:207px;background:var(--panel)}
.field-label{font-size:11px;color:#ddd}
.field{width:169px;height:20px;background:linear-gradient(#b8b8b8,#cfcfcf);border-radius:2px;border:1px solid #9a9a9a}
.field.tall{height:85px}
.form-btn{width:63px;height:20px;border-radius:2px;background:linear-gradient(#f6f6f6,#cfcfcf);color:#333;font-size:11.5px;text-align:center;line-height:20px}
.pay-title{font-size:11.5px;color:#ddd}
.card{height:26px;border-radius:2px;display:flex;align-items:center;justify-content:center;font-size:10px;font-weight:700;color:#fff;border:1px solid #eee;text-align:center;line-height:10px}
.footer-links{left:193px;top:1038px;font-size:11.5px;color:var(--muted)}
.footer-links span{margin:0 4px}
.copyright{left:193px;top:1058px;font-size:11.5px;color:var(--muted)}
.share{left:909px;top:1042px;width:119px;height:15px;background:#fff;border:1px solid #bbb;border-radius:2px;display:flex;align-items:center;gap:6px;padding-left:4px;font-size:8.5px;font-weight:700;color:#333;letter-spacing:.5px}
.share i{width:9px;height:9px;background:#f2583e;display:block}
</style>
</head>
<body>
<div class="abs header-band"></div>

<div class="abs brand"><span class="brand-dot"></span><span class="brand-name">TRELVEX</span></div>

<nav class="abs nav">
  <a class="active" href="#">Home</a>
  <a href="#">Our Services</a>
  <a href="#">Quotes</a>
  <a href="#">Links</a>
  <a href="#">Contact us</a>
</nav>

<div class="abs hero" role="img" aria-label="Electrician in a hard hat testing a switchboard with a clamp meter"></div>

<div class="abs cta-title"><b>CONTACT US</b> <i>TODAY!</i></div>
<div class="abs cta-sub">For your Domestic,<br>Commercial<br>&amp; Industrial sectors<br>services!</div>
<div class="abs cta-phone">02 5550 0137</div>
<a class="abs cta-btn" href="#">Click Here<br>For Quotation</a>

<div class="abs rule-h" style="left:184px;top:461px;width:853px"></div>
<div class="abs rule-v" style="left:818px;top:461px;height:558px"></div>

<p class="abs intro"><b>TRELVEX</b> is a new and rapidly expanding Electrical &amp; Communications Company that services the Domestic, Commercial &amp; Industrial sectors. Our service ranges from minor refurbishments to major installations, we also have a well maintained and efficient service team providing on-going support for all of your maintenance needs.</p>

<div class="abs sector" style="left:184px;top:547px">
  <div class="pic" role="img" aria-label="Two-storey family house with a green lawn" style="background:linear-gradient(#3b6fc4 0%,#8fb0da 40%,#c9c6bd 60%,#5a8a3a 100%)"></div>
  <div class="label">DOMESTIC</div>
</div>
<div class="abs sector" style="left:391px;top:547px">
  <div class="pic" role="img" aria-label="Office towers lit up at night" style="background:linear-gradient(90deg,#0e1a22 0%,#1c3a3a 40%,#1f4a68 70%,#123050 100%)"></div>
  <div class="label">COMMERCIAL</div>
</div>
<div class="abs sector" style="left:597px;top:547px">
  <div class="pic" role="img" aria-label="Industrial plant illuminated at dusk" style="background:linear-gradient(#2a4fa8 0%,#5a5a6a 45%,#c08a30 75%,#6a4a20 100%)"></div>
  <div class="label">INUSTRIAL</div>
</div>

<p class="abs pitch">We pride ourselves on our commitment to professionalism and our great attention to detail. We are gaining a reputation with our customers for our quality workmanship, friendly attitude &amp; reliable service.</p>

<div class="abs services-title">OUR SERVICES:</div>
<ul class="abs services">
  <li style="left:16px;top:18px">Air Conditioning</li>
  <li style="left:16px;top:41px">Lighting</li>
  <li style="left:16px;top:63px">Hot Water systems</li>
  <li style="left:16px;top:86px">Power Outlets</li>
  <li style="left:186px;top:18px">Electrical Services</li>
  <li style="left:186px;top:41px">Commercial Electrician</li>
  <li style="left:186px;top:63px">Test &amp; Tag</li>
  <li style="left:186px;top:86px">Phone &amp; data networking</li>
  <li style="left:384px;top:18px">Transformer/Switchboard Upgrades</li>
  <li style="left:384px;top:41px">Surge Protection</li>
  <li style="left:384px;top:63px">Commercial Electrical</li>
</ul>

<div class="abs form-panel"></div>
<div class="abs field-label" style="left:847px;top:490px">Name:</div>
<div class="abs field" style="left:847px;top:507px"></div>
<div class="abs field-label" style="left:847px;top:538px">Email:</div>
<div class="abs field" style="left:847px;top:555px"></div>
<div class="abs field-label" style="left:847px;top:586px">Subject:</div>
<div class="abs field" style="left:847px;top:603px"></div>
<div class="abs field-label" style="left:847px;top:633px">Message:</div>
<div class="abs field tall" style="left:847px;top:650px"></div>
<div class="abs form-btn" style="left:847px;top:749px">Send</div>
<div class="abs form-btn" style="left:953px;top:749px">Clear</div>

<div class="abs rule-h" style="left:818px;top:800px;width:219px"></div>
<div class="abs pay-panel"></div>
<div class="abs pay-title" style="left:847px;top:834px">Payment Options:</div>
<div class="abs card" style="left:847px;top:859px;width:45px;background:#1a3f8c">orbe</div>
<div class="abs card" style="left:897px;top:859px;width:43px;background:#1a3f8c;font-size:8.5px">Orbe Lite</div>
<div class="abs card" style="left:946px;top:859px;width:44px;background:#1a3f8c">Tallo</div>
<div class="abs card" style="left:847px;top:891px;width:45px;background:#1a3f8c;font-size:8px">lumo<br>charge</div>
<div class="abs card" style="left:897px;top:891px;width:70px;background:#f4f4f4;color:#1a3f8c;font-size:13px">bitfen</div>

<div class="abs rule-h" style="left:184px;top:1019px;width:853px"></div>
<div class="abs footer-links">Home<span>|</span>Our Services<span>|</span>Quotes<span>|</span>Links<span>|</span>Contact us</div>
<div class="abs copyright">© 2010 trelvex</div>
<div class="abs share"><i></i>SHARE</div>
</body>
</html>
```